Specialist Recruitment Process Outsourcing (RPO) company needs a modern, sleek website

We need a website which showcases our service offering, describes our onshore and offshore options. Our service is basically building teams of recruiters who become the outsourced (but in-house) recruiter for that specific client. Our logo colours include a light, bright green and a dark/midnight blue. This company will be targeting companies who need help with recruitment in technology, finance, engineering and other white collar industries. We are looking for a look and feeling that communicates cutting edge technology with a bright, energetic appeal. I will include some logo design files to work with.

Target Market(s)

Businesses: start ups who need to grow their staff, SMEs with regular recruitment needs, and larger businesses

Industry/Entity Type

Recruitment

Coding

Coded - Design and coding required

Number of Pages Required

4 page

Font styles to use
Sans Serif

Requirements
Must have
• Landing page should be highly visual, either with dynamic image or scrolling stills accompanies by our core service offering, values, and benefits.

A Services page will allows more detail about what we do, with a call to action.

A User Stories page will showcase some examples of how our services will help certain types of businesses.

Onshore/Offshore page will breakdown the benefits of both approaches and how combinations can work well.

Should fit the colour theming of our logo (files uploaded).

Nice to have
• Imagery can be both around business and people. We are looking for more of a "startup" feel than a corporate-y feel.

```html
<!DOCTYPE html>
<html lang="en">
<head>
<meta charset="utf-8">
<title>Crewline — Recruitment Process Outsourcing</title>
<link rel="stylesheet" href="https://fonts.googleapis.com/css2?family=Poppins:wght@500;600;700;800&family=Roboto:ital,wght@0,400;0,500;0,700;1,400&display=swap">
<style>
:root{
  --green:#00ec9c;
  --green-deep:#00d78d;
  --navy:#12142f;
  --navy-2:#1b2140;
  --ink:#16172b;
  --grey-text:#555a66;
  --light:#f1f1f3;
  --white:#ffffff;
}
*{box-sizing:border-box;margin:0;padding:0}
html,body{width:1200px;height:4286px;overflow:hidden}
body{font-family:'Roboto',sans-serif;color:var(--ink);background:var(--white);position:relative}
.abs{position:absolute}
.heading{font-family:'Poppins',sans-serif;font-weight:700;text-transform:uppercase;letter-spacing:-.3px}
section{position:absolute;left:0;width:1200px;overflow:hidden}

/* hero */
.hero{top:0;height:602px;background:linear-gradient(100deg,#3a2a22 0%,#6b5448 35%,#a59b95 60%,#c9c7c8 100%)}
.hero-photo{position:absolute;inset:0;background:linear-gradient(180deg,rgba(20,16,20,.15),rgba(20,16,20,.35))}
.brand{position:absolute;display:flex;flex-direction:column;align-items:center;gap:6px}
.brand-mark{width:26px;height:26px;border:3px solid var(--green)}
.brand-name{font-family:'Poppins',sans-serif;font-weight:600;font-size:12px;letter-spacing:3px;color:var(--green)}
.nav{position:absolute;top:38px;left:328px;display:flex;gap:14px;font-size:13px;color:#fff;font-family:'Roboto',sans-serif}
.nav .active{color:var(--green)}
.hero-title{left:113px;top:186px;font-size:58px;color:#fff;font-weight:800}
.hero-sub{left:113px;top:262px;font-size:35px;line-height:52px;color:#fff;font-weight:800}
.hero-sub .accent{color:var(--green)}
.btn{position:absolute;display:flex;align-items:center;justify-content:center;border-radius:22px;font-family:'Poppins',sans-serif;font-weight:600;font-size:14px;text-transform:uppercase}
.btn-green{background:var(--green);color:#fff}
.btn-navy{background:var(--navy);color:#fff}
.circle-arrow{position:absolute;width:36px;height:36px;border:1.5px solid rgba(255,255,255,.8);border-radius:50%}
.dots{left:499px;top:572px;display:flex;gap:6px}
.dots span{width:45px;height:3px;background:#fff}
.dots span.on{background:var(--green)}

/* services */
.services{top:602px;height:583px;background:var(--light)}
.center-title{position:absolute;left:0;width:1200px;text-align:center;font-size:40px;color:var(--ink)}
.center-sub{position:absolute;left:0;width:1200px;text-align:center;font-size:13px;line-height:26px;font-weight:500}
.service{position:absolute;width:300px;text-align:center}
.service-icon{width:68px;height:68px;margin:0 auto;border-radius:50%;background:var(--navy)}
.service-icon.green{background:var(--green)}
.service h3{margin-top:22px;font-size:25px;color:var(--ink)}
.service p{margin-top:18px;font-size:13px;line-height:25px;color:var(--grey-text)}
.vrule{position:absolute;width:1px;background:#8a8d96}

/* newsletter */
.newsletter{top:1185px;height:175px;background:var(--green)}
.newsletter h2{position:absolute;left:111px;top:70px;font-size:33px;color:#fff}
.email-field{position:absolute;left:679px;top:60px;width:338px;height:56px;border:1px solid #fff;color:#fff;font-size:16px;font-weight:500;padding:18px 22px}
.email-send{position:absolute;left:1017px;top:60px;width:70px;height:56px;background:var(--navy)}

/* value */
.value{top:1360px;height:610px;background:linear-gradient(90deg,#f2f2f2,#e6e6e6)}
.value-photo{position:absolute;left:715px;top:0;width:485px;height:610px;background:radial-gradient(circle at 50% 55%,#6d6560 0%,#a5a09c 35%,#d8d8d8 70%,#ececec 100%)}
.value h2{position:absolute;left:111px;top:75px;font-size:42px;color:var(--ink)}
.value .lead{position:absolute;left:111px;top:142px;font-size:18px;line-height:30px;width:460px}
.value-card{position:absolute;top:232px;width:304px;height:294px;padding:50px 24px 0}
.value-card h3{font-size:24px;line-height:35px;color:#fff}
.value-card p{margin-top:10px;font-size:13px;line-height:28px;color:#fff}
.value-card.navy{left:111px;background:var(--navy)}
.value-card.green{left:414px;background:var(--green)}

/* stories */
.stories{top:1970px;height:580px;background:linear-gradient(135deg,#00e796,#00d98d 50%,#00ed9f)}
.stories .center-title,.stories .center-sub{color:#fff}
.story{position:absolute;top:207px;width:303px;height:289px;background:#fff;border-bottom:8px solid var(--navy);padding:32px 24px 0}
.stars{color:#f4a300;font-size:17px;letter-spacing:1px}
.g-dot{position:absolute;right:24px;top:30px;width:26px;height:26px;border-radius:50%;background:#d5d7dc}
.story blockquote{margin-top:24px;font-style:italic;font-size:16.5px;line-height:28.5px;color:#333;text-align:justify}
.story .author{margin-top:18px;font-size:18px;font-weight:500}

/* leader */
.leader{top:2550px;height:570px;background:linear-gradient(110deg,#1a2040,#2a3152 50%,#1c2342)}
.avatar{position:absolute;left:111px;top:2650px;width:102px;height:102px;border-radius:50%;background:#7d8898;border:3px solid var(--green)}
.leader-name{position:absolute;left:235px;top:116px;font-size:36px;color:#fff}
.leader-name span{color:var(--green)}
.leader-role{position:absolute;left:235px;top:162px;font-size:12px;color:#fff;letter-spacing:.2px}
.leader-bio{position:absolute;left:111px;top:222px;width:460px;font-size:14px;line-height:28px;color:#e4e6ee}
.social{position:absolute;display:flex}
.social span{border:1.5px solid #fff;border-radius:50%}
.stat{position:absolute;left:641px;width:110px;height:110px;border:2px solid #fff;border-radius:50%;display:flex;align-items:center;justify-content:center;font-family:'Poppins',sans-serif;font-weight:600;font-size:29px;color:var(--green)}
.stat-text{position:absolute;left:770px;width:330px}
.stat-text h4{font-family:'Poppins',sans-serif;font-weight:500;font-size:24px;color:#fff}
.stat-text p{margin-top:6px;font-size:13px;line-height:27px;color:#e0e2ea}

/* news */
.news{top:3120px;height:634px;background:#fff}
.news-card{position:absolute;top:157px;width:310px;height:392px;background:#fff;box-shadow:0 2px 10px rgba(0,0,0,.12)}
.news-img{height:196px;background:linear-gradient(135deg,#c8c9cc,#8f939a)}
.news-card h3{padding:22px 10px 0;font-size:17px;line-height:28px;color:var(--ink);letter-spacing:0}
.news-card p{padding:8px 10px 0;font-size:13px;line-height:26px;color:var(--grey-text)}
.news-card .more{padding:12px 10px 0;font-size:15px;font-weight:500;text-transform:uppercase}

/* contact */
.contact{top:3754px;height:532px;background:var(--navy)}
.contact h2{position:absolute;left:111px;top:68px;font-size:46px;line-height:56px;color:#fff}
.underline{position:absolute;left:111px;top:188px;width:117px;height:4px;background:var(--green)}
.label{position:absolute;font-family:'Poppins',sans-serif;font-weight:600;font-size:17px;color:#fff;text-transform:uppercase}
.info{position:absolute;font-family:'Poppins',sans-serif;font-size:16px;line-height:25px;color:var(--green)}
.field{position:absolute;left:679px;width:409px;border:1px solid #fff;color:#fff;font-family:'Poppins',sans-serif;font-weight:500;font-size:14px;padding:0 22px;display:flex;align-items:center}
.submit{position:absolute;left:957px;top:424px;width:131px;height:42px;background:var(--green);color:#fff;font-family:'Poppins',sans-serif;font-weight:600;font-size:18px;display:flex;align-items:center;justify-content:center}
.copyright{position:absolute;left:0;top:486px;width:1200px;text-align:center;font-size:14px;color:#fff}
</style>
</head>
<body>

<section class="hero">
  <div class="hero-photo" role="img" aria-label="Photo of a business team meeting around a table in a bright office"></div>
  <div class="brand" style="left:112px;top:12px">
    <span class="brand-mark"></span>
    <span class="brand-name">CREWLINE</span>
  </div>
  <nav class="nav">
    <span class="active">HOME</span><span>/</span><span>ABOUT</span><span>/</span><span>OUR SERVICES</span><span>/</span><span>USER STORIES</span><span>/</span><span>ONSHORE | OFFSHORE</span><span>/</span><span>CONTACT US</span>
  </nav>
  <h1 class="abs heading hero-title">Crewline</h1>
  <div class="abs heading hero-sub">Recruitment Process<br>Outsourcing <span class="accent">with</span><br><span class="accent">Growth Ambitions</span></div>
  <a class="btn btn-green" style="left:115px;top:429px;width:150px;height:40px">Get Started</a>
  <span class="circle-arrow" style="left:55px;top:283px"></span>
  <span class="circle-arrow" style="left:1109px;top:283px"></span>
  <svg class="abs" style="left:55px;top:283px" width="36" height="36"><path d="M21 11l-7 7 7 7" stroke="#fff" stroke-width="1.5" fill="none"/></svg>
  <svg class="abs" style="left:1109px;top:283px" width="36" height="36"><path d="M15 11l7 7-7 7" stroke="#fff" stroke-width="1.5" fill="none"/></svg>
  <div class="abs dots"><span></span><span class="on"></span><span></span><span></span></div>
</section>

<section class="services">
  <h2 class="heading center-title" style="top:76px">Our Services</h2>
  <p class="center-sub" style="top:130px">Lorem ipsum dolor sit amet, consectetur adipiscing elit, sed do eiusmod tempor incididunt ut labore<br>et dolore magna aliqua. Quis ipsum suspendisse ultrices gravida.</p>
  <div class="service" style="left:110px;top:205px">
    <div class="service-icon" role="img" aria-label="Globe with people icon"></div>
    <h3 class="heading">Outsourcing</h3>
    <p>Lorem ipsum dolor sit met, consectur adipiscing elit, sed do eiusmod tempor incididunt ut labore et dolore magna aliqua. Quis ipsum suspendisse ultrices gravida. Risus commodo</p>
  </div>
  <div class="service" style="left:450px;top:205px">
    <div class="service-icon green" role="img" aria-label="Connected team icon"></div>
    <h3 class="heading">Onshore</h3>
    <p>Lorem ipsum dolor sit met, consectur adipiscing elit, sed do eiusmod tempor incididunt ut labore et dolore magna aliqua. Quis ipsum suspendisse ultrices gravida. Risus commodo</p>
  </div>
  <div class="service" style="left:790px;top:205px">
    <div class="service-icon" role="img" aria-label="Handshake icon"></div>
    <h3 class="heading">Offshore</h3>
    <p>Lorem ipsum dolor sit met, consectur adipiscing elit, sed do eiusmod tempor incididunt ut labore et dolore magna aliqua. Quis ipsum suspendisse ultrices gravida. Risus commodo</p>
  </div>
  <span class="vrule" style="left:429px;top:222px;height:263px"></span>
  <span class="vrule" style="left:769px;top:222px;height:263px"></span>
  <a class="btn btn-navy" style="left:179px;top:456px;width:162px;height:40px">View More</a>
  <a class="btn btn-green" style="left:519px;top:456px;width:162px;height:40px">View More</a>
  <a class="btn btn-navy" style="left:859px;top:456px;width:162px;height:40px">View More</a>
  <svg class="abs" style="left:64px;top:338px" width="16" height="28"><path d="M13 2L3 14l10 12" stroke="#555" stroke-width="1.5" fill="none"/></svg>
  <svg class="abs" style="left:1114px;top:338px" width="16" height="28"><path d="M3 2l10 12L3 26" stroke="#555" stroke-width="1.5" fill="none"/></svg>
</section>

<section class="newsletter">
  <h2 class="heading">Subscribe to Newsletter</h2>
  <div class="email-field">Your Email</div>
  <div class="email-send">
    <svg width="70" height="56"><path d="M24 29l22-10-8 20-4-7z" fill="#fff"/><path d="M34 32l12-13" stroke="#12142f" stroke-width="1.5"/></svg>
  </div>
</section>

<section class="value">
  <div class="value-photo" role="img" aria-label="Overhead photo of a team working around a round table with a tablet and papers"></div>
  <h2 class="heading">Our Value</h2>
  <p class="lead">Lorem ipsum dolor sit amet, consectetur adipiscing elit, sed do eiusmod tempor incididunt</p>
  <div class="value-card navy">
    <h3 class="heading">Seed and Early<br>Stage Companies</h3>
    <p>Lorem ipsum dolor sit amet, consectetur adipiscing elit, sed do eiusmod incididunt ut labore et dolore magna ua. Quis ipsum suspendisse ultrices gravida.</p>
  </div>
  <div class="value-card green">
    <h3 class="heading">Growth and Late<br>Stage Companies</h3>
    <p>Lorem ipsum dolor sit amet, consectetur adipiscing elit, sed do eiusmod incididunt ut labore et dolore magna ua. Quis ipsum suspendisse ultrices gravida.</p>
  </div>
</section>

<section class="stories">
  <h2 class="heading center-title" style="top:76px">User Stories</h2>
  <p class="center-sub" style="top:128px">Lorem ipsum dolor sit amet, consectetur adipiscing elit, sed do eiusmod tempor incididunt ut<br>labore et dolore magna aliqua. Quis ipsum suspendisse ultrices gravida.</p>
  <article class="story" style="left:116px">
    <div class="stars">★★★★★</div><span class="g-dot"></span>
    <blockquote>Lorem ictetur adipiscing elit, sed do eiusmod tempor incididunt ut labore et dolore magna aliqua. Quis ipsum suspendisse ultrices gravida.</blockquote>
    <div class="author">- Sam Carter</div>
  </article>
  <article class="story" style="left:454px">
    <div class="stars">★★★★★</div><span class="g-dot"></span>
    <blockquote>Lorem ictetur adipiscing elit, sed do eiusmod tempor incididunt ut labore et dolore magna aliqua. Quis ipsum suspendisse ultrices gravida.</blockquote>
    <div class="author">- Sam Carter</div>
  </article>
  <article class="story" style="left:790px">
    <div class="stars">★★★★★</div><span class="g-dot"></span>
    <blockquote>Lorem ictetur adipiscing elit, sed do eiusmod tempor incididunt ut labore et dolore magna aliqua. Quis ipsum suspendisse ultrices gravida.</blockquote>
    <div class="author">- Sam Carter</div>
  </article>
</section>

<section class="leader" role="img" aria-label="Dim background photo of an office team">
  <h2 class="heading leader-name">Daniel <span>Reyes</span></h2>
  <div class="leader-role">MANAGING DIRECTOR | CHIEF PERSPECTIVE</div>
  <p class="leader-bio">Lorem ipsum dolor sit amet, consectetur adipiscseo eiusmod tempor incididunt ut labore et dolore magna aliqua. ipsum spendisse ultrices gravida. Risus commodo viverra maecenus vel facilisis. Lorem ipsum dolor sit amet, consectetur adipiscing elit, sed do tempor ididunt ut labore et dolore magna aliqua. Quis ipsus a. Risus commodo viverra maecenas accumsan lacus vel facilisis. Lorem ipsum dolor sit amet, consectetur adipiscseo eiusmod</p>
  <div class="social" style="left:110px;top:449px;gap:8px">
    <span style="width:36px;height:36px"></span><span style="width:36px;height:36px"></span><span style="width:36px;height:36px"></span><span style="width:36px;height:36px"></span>
  </div>
  <span class="vrule" style="left:601px;top:84px;height:405px;background:#9aa0b4"></span>
  <div class="stat" style="top:101px">10+</div>
  <div class="stat-text" style="top:110px"><h4>year’s Experience</h4><p>Lorem ipsum dolor sit amet, consectetur ing elit,<br>sed do eiusmod tempor incididunt ut</p></div>
  <div class="stat" style="top:239px">200+</div>
  <div class="stat-text" style="top:248px"><h4>Public &amp; Private Companies</h4><p>Lorem ipsum dolor sit amet, consectetur ing elit,<br>sed do eiusmod tempor incididunt ut</p></div>
  <div class="stat" style="top:375px">100%</div>
  <div class="stat-text" style="top:384px"><h4>Satisfaction</h4><p>Lorem ipsum dolor sit amet, consectetur ing elit,<br>sed do eiusmod tempor incididunt ut</p></div>
</section>
<div class="avatar" role="img" aria-label="Portrait photo of the managing director"></div>

<section class="news">
  <h2 class="heading center-title" style="top:76px">News and Insights</h2>
  <article class="news-card" style="left:111px">
    <div class="news-img" role="img" aria-label="Photo of colleagues collaborating at a desk"></div>
    <h3 class="heading">Lorem ipsum dolor sitamet,<br>consectetur adipiscing</h3>
    <p>Lorem ipsum dolor sit amet, ctetur adipiscing elit, sed do eiusmod tempor incit ut labore et dolore magna aliqua.</p>
    <div class="more">Continue Reading</div>
  </article>
  <article class="news-card" style="left:444px">
    <div class="news-img" role="img" aria-label="Photo of hands pointing at charts beside a laptop"></div>
    <h3 class="heading">Lorem ipsum dolor sitamet,<br>consectetur adipiscing</h3>
    <p>Lorem ipsum dolor sit amet, ctetur adipiscing elit, sed do eiusmod tempor incit ut labore et dolore magna aliqua.</p>
    <div class="more">Continue Reading</div>
  </article>
  <article class="news-card" style="left:777px">
    <div class="news-img" role="img" aria-label="Photo of a smiling team gathered around a laptop"></div>
    <h3 class="heading">Lorem ipsum dolor sitamet,<br>consectetur adipiscing</h3>
    <p>Lorem ipsum dolor sit amet, ctetur adipiscing elit, sed do eiusmod tempor incit ut labore et dolore magna aliqua.</p>
    <div class="more">Continue Reading</div>
  </article>
</section>

<section class="contact">
  <h2 class="heading">Get in Touch<br>With Us</h2>
  <span class="underline"></span>
  <div class="brand" style="left:114px;top:222px">
    <span class="brand-mark" style="border-color:#fff"></span>
    <span class="brand-name" style="color:#fff">CREWLINE</span>
  </div>
  <div class="label" style="left:356px;top:234px">Telephone</div>
  <div class="info" style="left:356px;top:258px">+000 555 0199</div>
  <div class="label" style="left:111px;top:311px">Direct Message</div>
  <div class="info" style="left:111px;top:335px;width:210px">City name 10150, United States</div>
  <div class="label" style="left:356px;top:311px">Direct Message</div>
  <div class="info" style="left:356px;top:335px">hello@crewline.example</div>
  <div class="social" style="left:114px;top:397px;gap:11px">
    <span style="width:44px;height:44px"></span><span style="width:44px;height:44px"></span><span style="width:44px;height:44px"></span><span style="width:44px;height:44px"></span>
  </div>
  <div class="field" style="top:77px;height:57px">FULL NAME</div>
  <div class="field" style="top:146px;height:57px">EMAIL</div>
  <div class="field" style="top:215px;height:57px">SUBJECT</div>
  <div class="field" style="top:285px;height:126px;align-items:flex-start;padding-top:20px">HOW CAN WE HELP YOU</div>
  <div class="submit">SUBMIT</div>
  <div class="copyright">Crewline © 2020 All Rights Reserved | Privacy Policy</div>
</section>

</body>
</html>
```